Create a bold and border around my logo to make it pop and sign graphic design

I would like someone to create a sign graphic design so I can use on the side of my trucks and put on yard signs. I would to remove a lot of the white and add more of the orange and blue to give it more pop when cars drive past. I would like the services to be removed and for you to leave space for a mobile number that i would add later. I don’t want my logo changed at all. I just want colour and design to be added to the background so i can use it in signage. Same colour as on the sign

```html
<!DOCTYPE html>
<html lang="en">
<head>
<meta charset="utf-8">
<title>Branchworthy – Truck Sign</title>
<link rel="stylesheet" href="https://fonts.googleapis.com/css2?family=Montserrat:wght@600;700&display=swap">
<style>
  :root {
    --backdrop: #1a0803;
    --orange: #d64a04;
    --orange-deep: #c93302;
    --white: #ffffff;
    --navy: #03306f;
    --navy-light: #0a4290;
  }
  html, body {
    margin: 0;
    padding: 0;
    width: 1200px;
    height: 709px;
    overflow: hidden;
    background: var(--backdrop);
    font-family: "Montserrat", sans-serif;
  }
  .sign {
    position: absolute;
    left: 30px;
    top: 113px;
    width: 1140px;
    height: 483px;
    overflow: hidden;
  }
  .band { position: absolute; left: 0; width: 100%; }
  .band--top {
    top: 0; height: 173px;
    background: linear-gradient(135deg, var(--orange) 0%, var(--orange-deep) 45%, var(--orange) 62%, var(--orange-deep) 85%, var(--orange) 100%);
  }
  .band--middle { top: 173px; height: 137px; background: var(--white); }
  .band--bottom {
    top: 310px; height: 173px;
    background: linear-gradient(90deg, var(--navy) 0%, var(--navy-light) 50%, var(--navy) 100%);
  }
  .badge {
    position: absolute;
    left: 23px;
    top: 66px;
    width: 352px;
    height: 352px;
    border-radius: 50%;
    background: var(--white);
  }
  .brand-name {
    position: absolute;
    left: 385px;
    top: 206px;
    margin: 0;
    font-weight: 700;
    font-size: 68px;
    line-height: 1;
    letter-spacing: 1px;
    color: var(--navy);
  }
  .phone {
    position: absolute;
    left: 385px;
    top: 348px;
    display: flex;
    align-items: center;
    gap: 14px;
    color: var(--white);
    font-weight: 600;
    font-size: 100px;
    line-height: 1;
    letter-spacing: -1px;
  }
  .phone__icon { width: 66px; height: 86px; }
</style>
</head>
<body>
  <div class="sign">
    <div class="band band--top"></div>
    <div class="band band--middle"></div>
    <div class="band band--bottom"></div>
    <div class="badge"></div>
    <h1 class="brand-name">BRANCHWORTHY</h1>
    <div class="phone">
      <svg class="phone__icon" viewBox="0 0 24 30" aria-hidden="true">
        <path fill="#ffffff" d="M5 1c1-.6 2.2-.3 2.8.7l2.6 4.6c.6 1 .3 2.2-.6 2.8l-1.8 1.2c-.4.3-.5.8-.3 1.3 1.3 3.8 3.4 7.3 6.2 10.2.4.4.9.4 1.3.2l1.9-1.1c1-.6 2.2-.3 2.8.6l2.8 4.4c.6 1 .4 2.2-.5 2.8l-2.2 1.5c-1.2.8-2.8 1-4.2.4C9.6 27.8 3.6 19.6 1.4 10.6 1 9 1.4 7.4 2.5 6.3z"/>
      </svg>
      <span class="phone__number">0123456789</span>
    </div>
  </div>
</body>
</html>
```